Zelno Vigor Iron Tempo Multi Vitamin Label Design

We need a label design for our Sports Performance Daily Multi Vitamin specially created and branded for our Zelno Vigor line for the University of Calvoria. The feel is edgy, sports nutrition. Two logos need to be incorporated... Zelno and the Collective Logo attached. The colors should be the official colors of the University of Calvoria. The font may also be the Georgia font... or the Zelno font. Or any font. A hydration product will also be created later on...so this label design may be used on many products. Please utilize the collective logo similar to the use in the attached photo. No official trademark items from the University of Calvoria should be used. Attached is also an image if the bottle (white) that will be used for the vitamin. Please use red, black, grey, white. We are looking for the front design only right now and once selected, will work on the nutrition/back label portion with the artist.

```html
<!DOCTYPE html>
<html lang="en">
<head>
<meta charset="utf-8">
<title>Zelno Vigor Multi Vitamin Label</title>
<link href="https://fonts.googleapis.com/css2?family=Montserrat:wght@600;800&display=swap" rel="stylesheet">
<style>
  :root {
    --stage: #1b1b1b;
    --label-red: #f8141f;
    --ink-black: #050505;
    --band-red: #e3101b;
    --paper-white: #ffffff;
  }
  * { box-sizing: border-box; margin: 0; padding: 0; }
  html, body {
    width: 1200px;
    height: 1200px;
    overflow: hidden;
    background: var(--stage);
  }
  .canvas {
    position: relative;
    width: 1200px;
    height: 1200px;
  }
  .label {
    position: absolute;
    left: 100px;
    top: 182px;
    width: 1000px;
    height: 837px;
    background: var(--label-red);
  }
  .brush-field {
    position: absolute;
    left: 190px;
    top: 100px;
    width: 630px;
    height: 645px;
    background: var(--ink-black);
    border-radius: 40px 70px 50px 60px;
  }
  .collective-mark {
    position: absolute;
    left: 0;
    top: 190px;
    width: 1000px;
    display: flex;
    justify-content: center;
    align-items: center;
    gap: 10px;
    font-family: "Montserrat", sans-serif;
    font-weight: 600;
    font-size: 16px;
    letter-spacing: 2px;
    text-transform: uppercase;
    color: var(--paper-white);
  }
  .collective-mark .dot {
    width: 14px;
    height: 14px;
    border-radius: 50%;
    background: var(--paper-white);
  }
  .brand-name {
    position: absolute;
    left: 0;
    top: 280px;
    width: 1000px;
    text-align: center;
    font-family: "Montserrat", sans-serif;
    font-weight: 800;
    font-size: 110px;
    letter-spacing: 4px;
    color: var(--paper-white);
  }
  .line-band {
    position: absolute;
    left: 255px;
    top: 432px;
    width: 500px;
    height: 70px;
    background: var(--band-red);
  }
  .line-name {
    position: absolute;
    left: 0;
    top: 428px;
    width: 1000px;
    text-align: center;
    font-family: "Montserrat", sans-serif;
    font-weight: 800;
    font-size: 64px;
    letter-spacing: 6px;
    color: var(--paper-white);
  }
  .product-type {
    position: absolute;
    left: 0;
    top: 548px;
    width: 1000px;
    text-align: center;
    font-family: "Montserrat", sans-serif;
    font-weight: 600;
    font-size: 27px;
    letter-spacing: 3px;
    color: var(--paper-white);
  }
</style>
</head>
<body>
<div class="canvas">
  <div class="label">
    <div class="brush-field" role="img" aria-label="Rough black paint brush strokes behind the brand lockup"></div>
    <div class="collective-mark"><span class="dot"></span><span>Calvoria Collective</span></div>
    <div class="brand-name">ZELNO</div>
    <div class="line-band"></div>
    <div class="line-name">VIGOR</div>
    <div class="product-type">MULTI VITAMIN</div>
  </div>
</div>
</body>
</html>
```